Bright Meadow Care Partners, LLC

We are private duty home care agency. We provide in-home care for people of all ages. Our kind natured and patient caregivers provide assistance to those who have difficulty with caring for themselves. We already have a logo designed by ArtNestly

```html
<!DOCTYPE html>
<html lang="en">
<head>
<meta charset="utf-8">
<title>Bright Meadow Care Partners, LLC</title>
<link rel="stylesheet" href="https://fonts.googleapis.com/css2?family=Roboto:ital,wght@0,400;0,500;0,700;1,400&display=swap">
<style>
:root{
  --brand-green:#379c00;
  --brand-orange:#f9530b;
  --lime:#7ff53a;
  --ink:#1c1c1c;
  --ink-soft:#444;
  --white:#ffffff;
  --hero-bg:#e7ece9;
  --care-blue:#ddeff5;
  --form-bg:#f5f5f5;
  --line:#cfcfcf;
  --placeholder:#c4c4c4;
  --icon-blue:#3b5998;
  --icon-mail:#4aa3cf;
}
*{box-sizing:border-box;margin:0;padding:0}
html,body{width:718px;height:1200px;overflow:hidden}
body{background:var(--brand-green);font-family:'Roboto',sans-serif;color:var(--ink);position:relative}
.abs{position:absolute}
.page-card{left:90px;top:34px;width:539px;height:1136px;background:var(--white);border-radius:4px}

.brand-name{color:var(--brand-green);font-weight:700;line-height:1;letter-spacing:-.3px}
.brand-header{left:118px;top:72px;font-size:23px}
.brand-header .brand-mark{display:inline-block;width:14px;height:14px;background:var(--brand-orange);border-radius:50%;margin-right:6px;vertical-align:1px}
.brand-footer{left:390px;top:1117px;font-size:12px}

.header-contact{right:117px;top:55px;text-align:right;font-size:10.5px;line-height:13px}
.header-contact .cta{color:var(--brand-orange)}
.header-contact .cta b{font-weight:700}
.header-contact .numbers{color:var(--ink-soft);margin-top:3px;line-height:12.5px;font-size:10px}
.social{display:flex;gap:5px}
.social-header{right:117px;top:113px}
.social-footer{left:118px;top:1119px}
.icon{width:18px;height:18px;border-radius:1px}
.icon-mail{background:var(--icon-mail)}
.icon-social{background:var(--icon-blue)}

.main-nav{left:90px;top:157px;width:539px;height:32px;background:var(--brand-orange)}
.main-nav a{position:absolute;top:9px;color:var(--white);font-size:10.5px;font-weight:500;text-decoration:none}

.hero{left:90px;top:189px;width:539px;height:210px;background:var(--hero-bg)}
.hero-photo{left:0;top:0;width:320px;height:210px;background:linear-gradient(90deg,#7fa3c7 0%,#a9bfd6 45%,#dfe6e8 100%)}
.hero-title{left:308px;top:40px;font-size:20px;line-height:24px;font-weight:500;letter-spacing:.3px;color:var(--ink)}
.hero-sub{left:308px;top:88px;font-size:10px;line-height:12.5px;color:#333;font-weight:500}
.btn{background:var(--lime);color:var(--white);font-weight:500;display:flex;align-items:center;justify-content:center}
.hero-btn{left:308px;top:123px;width:101px;height:26px;font-size:10.5px}

.section-title{color:var(--brand-orange);font-size:20px;line-height:24.5px;font-weight:500;letter-spacing:.8px}
.companion-photo{left:348px;top:425px;width:217px;height:193px;background:linear-gradient(90deg,#ffffff 0%,#e9eef3 25%,#cdd8e2 60%,#e6e3de 100%)}
.companion-title{right:374px;top:446px;text-align:right}
.companion-lead{right:374px;top:503px;text-align:right;font-size:10.3px;line-height:12px;font-weight:500}
.companion-body{right:374px;top:553px;width:180px;text-align:right;font-size:7.4px;line-height:9.4px;color:#222}

.care-band{left:151px;top:647px;width:416px;height:146px;background:var(--care-blue)}
.care-photo{left:0;top:0;width:205px;height:146px;background:linear-gradient(90deg,#dcdcda 0%,#ecebe8 50%,#dbe9ee 100%)}
.care-title{left:213px;top:24px}
.care-body{left:213px;top:86px;width:200px;font-size:7.4px;line-height:9.4px;color:#222}

.contact-panel{left:151px;top:793px;width:416px;height:280px;background:var(--form-bg)}
.contact-photo{left:186px;top:0;width:230px;height:280px;background:linear-gradient(90deg,rgba(245,245,245,1) 0%,#ececec 35%,#e6e6e6 100%)}
.contact-copy{right:247px;top:9px;text-align:right}
.contact-heading{font-size:12.5px;line-height:16px;font-weight:500;letter-spacing:.3px}
.contact-label{color:var(--brand-orange);font-size:10px;font-weight:500;margin-top:13px;line-height:11px}
.contact-small{font-size:7.4px;line-height:9px;color:#222}
.field{left:44px;width:126px;height:21px;background:var(--white);border:1px solid var(--line);font-size:7.4px;font-style:italic;color:var(--placeholder);text-align:right;padding:6px 6px 0 0}
.field-area{height:38px}
.send-btn{left:69px;top:234px;width:101px;height:25px;font-size:10px}

.footer-divider{left:494px;top:1110px;width:1.5px;height:37px;background:var(--brand-green)}
.footer-contact{right:117px;top:1116px;text-align:right;font-size:10px;line-height:12.5px;color:var(--ink-soft)}
.copyright{left:0;top:1175px;width:718px;text-align:center;color:var(--white);font-size:7.4px}
</style>
</head>
<body>
<div class="abs page-card"></div>

<header>
  <div class="abs brand-name brand-header"><span class="brand-mark"></span>Bright Meadow<br><span style="padding-left:20px">Care Partners</span></div>
  <div class="abs header-contact">
    <div class="cta">Call Us for <b>FREE</b><br>In-Home Assessment</div>
    <div class="numbers">Phone : 248-555-0136<br>Fax : 248-555-0179</div>
  </div>
  <div class="abs social social-header"><span class="icon icon-mail"></span><span class="icon icon-social"></span></div>
</header>

<nav class="abs main-nav">
  <a href="#" style="left:129px">Home</a>
  <a href="#" style="left:193px">About Us</a>
  <a href="#" style="left:267px">Our Services</a>
  <a href="#" style="left:357px">Contact Us</a>
</nav>

<section class="abs hero">
  <div class="abs hero-photo" role="img" aria-label="Smiling caregiver in blue scrubs with medical team behind her"></div>
  <h1 class="abs hero-title">LIVE INDEPENDENTLY<br>IN YOUR OWN HOME</h1>
  <p class="abs hero-sub">We provide in-home care<br>for people of all ages</p>
  <div class="abs btn hero-btn">Contact Us</div>
</section>

<section>
  <h2 class="abs section-title companion-title">COMPANION AND<br>PERSONAL CARE</h2>
  <p class="abs companion-lead">24-Hours Live-in, Overnight,<br>Full Time, Part Time, Respite Care<br>and more</p>
  <p class="abs companion-body">We tailor each plan of care to the needs of our clients. Our care plan includes input from the client, the medical team, family members, and all those providing services</p>
  <div class="abs companion-photo" role="img" aria-label="Doctors reviewing a tablet together"></div>
</section>

<section class="abs care-band">
  <div class="abs care-photo" role="img" aria-label="Caregiver holding a patient's hands across a desk"></div>
  <h2 class="abs section-title care-title">EXCEPTIONAL<br>ONE ON ONE CARE</h2>
  <p class="abs care-body">Our kind natured and patient caregivers provide assistance to those who have difficulty with caring for themselves</p>
</section>

<section class="abs contact-panel">
  <div class="abs contact-photo" role="img" aria-label="Hands typing on a laptop keyboard, faded"></div>
  <div class="abs contact-copy">
    <h3 class="contact-heading">FOR MORE<br>INFORMATIONS</h3>
    <div class="contact-label">CALL US NOW</div>
    <div class="contact-small">Phone : 248-555-0136<br>Fax : 248-555-0179</div>
    <div class="contact-label" style="margin-top:12px">OR FILL THE FORM</div>
    <div class="contact-small">We'll contact you as soon as possible</div>
  </div>
  <div class="abs field" style="top:120px">Name</div>
  <div class="abs field" style="top:144px">Email</div>
  <div class="abs field" style="top:168px">Phone number</div>
  <div class="abs field field-area" style="top:192px">Additional information</div>
  <div class="abs btn send-btn">Send</div>
</section>

<footer>
  <div class="abs social social-footer"><span class="icon icon-mail"></span><span class="icon icon-social"></span></div>
  <div class="abs brand-name brand-footer">Bright Meadow<br>Care Partners</div>
  <div class="abs footer-divider"></div>
  <div class="abs footer-contact">Phone : 248-555-0136<br>Fax : 248-555-0179</div>
  <div class="abs copyright">Copyright 2019. All Rights Reserved.</div>
</footer>
</body>
</html>
```